Design and Renovation Company Luxury Business Card

I want to create a luxury business card for a Design and Renovation Firm . We will use our current logo. The company name is 742BUILD. We do not want anything standard. We need a very unique concept.
Please see uploaded inspiration. I really like the textured paper option. I would like the card to be thick with debossing, and/or embossing options. The logo has orange in it but I would like to see the card with and without the orange. I think the orange may make the company feel less high-end. The goal is to elevate the logo not match its vibe per se of the logo. We want something very unique, not standard at all!
I would like a space for :
Logo,
Name,
Position,
Email,
Office number,
Website Address,
Business Address,
Thank you!
Have fun!
Target Market(s)
Home owners Age 35 +
Industry/Entity Type
Design and Renovation
Contact Information for Business Card
Logo, Name, Position, Email, Office number, Website Address, Business Address,.
Colors
Designer to choose colors to be used in the design.
Requirements
Must have
- A luxury designer feel. Must be black or dark grey but open to other luxury ideas.
Nice to have
- Gold, silver, black embossing or debossing. Textured paper design.
Should not have
- A cheap look and feel.

```html
<!DOCTYPE html>
<html lang="en">
<head>
<meta charset="utf-8">
<title>742BUILD Business Card</title>
<link rel="stylesheet" href="https://fonts.googleapis.com/css2?family=DM+Sans:wght@400;500;700&display=swap">
<style>
  :root {
    --backdrop: #b3b3b3;
    --paper: #ffffff;
    --ink: #060709;
    --accent: #f7941d;
    --reverse: #ffffff;
  }
  * { margin: 0; padding: 0; box-sizing: border-box; }
  html, body { width: 1200px; height: 1200px; overflow: hidden; }
  body {
    background: var(--backdrop);
    position: relative;
    font-family: "DM Sans", Arial, sans-serif;
  }
  .card {
    position: absolute;
    left: 176px;
    width: 843px;
    height: 494px;
    background: var(--paper);
    overflow: hidden;
  }
  .card--front { top: 81px; }
  .card--back { top: 625px; }

  .block { position: absolute; }
  .ink { background: var(--ink); }
  .accent { background: var(--accent); }

  /* front */
  .contact-panel { left: 30px; top: 56px; width: 341px; height: 380px; }
  .panel-tab { left: 371px; top: 56px; width: 15px; height: 160px; }
  .panel-foot { left: 327px; top: 436px; width: 15px; height: 36px; }

  .person-name {
    position: absolute; left: 75px; top: 112px;
    color: var(--reverse); font-weight: 700; font-size: 35px; line-height: 1.1;
  }
  .person-role {
    position: absolute; left: 75px; top: 153px;
    color: var(--reverse); font-size: 21px;
  }
  .contact-list { position: absolute; left: 79px; top: 216px; list-style: none; }
  .contact-list li {
    display: flex; align-items: flex-start;
    color: var(--reverse); font-size: 21px; line-height: 28px; margin-bottom: 8px;
  }
  .contact-list svg { width: 18px; height: 18px; margin: 5px 7px 0 0; flex: none; fill: var(--accent); }
  .contact-list .web { color: var(--accent); font-weight: 700; }

  .front-wordmark {
    position: absolute; left: 506px; top: 356px;
    font-weight: 500; font-size: 52px; letter-spacing: 2px;
    color: var(--ink); line-height: 1;
  }

  /* back */
  .rule-top { left: 82px; top: 39px; width: 725px; height: 35px; }
  .tab-top { left: 734px; top: 0; width: 35px; height: 113px; }
  .tab-bottom { left: 39px; top: 380px; width: 36px; height: 114px; }
  .rule-bottom { left: 0; top: 419px; width: 725px; height: 35px; }

  .back-wordmark {
    position: absolute; left: 268px; top: 196px;
    font-weight: 500; font-size: 82px; letter-spacing: 3px;
    color: var(--ink); line-height: 1;
  }
  .tagline {
    position: absolute; left: 276px; top: 275px;
    font-weight: 500; font-size: 18px; letter-spacing: 3.6px;
    color: var(--ink); line-height: 1.2;
  }
</style>
</head>
<body>
  <section class="card card--front">
    <div class="block ink contact-panel"></div>
    <div class="block accent panel-tab"></div>
    <div class="block accent panel-foot"></div>

    <h1 class="person-name">YOUR NAME</h1>
    <p class="person-role">Designation</p>
    <ul class="contact-list">
      <li><svg viewBox="0 0 24 24"><path d="M6.6 10.8a15 15 0 0 0 6.6 6.6l2.2-2.2a1 1 0 0 1 1-.25 11.4 11.4 0 0 0 3.6.57 1 1 0 0 1 1 1V20a1 1 0 0 1-1 1A17 17 0 0 1 3 4a1 1 0 0 1 1-1h3.5a1 1 0 0 1 1 1c0 1.25.2 2.45.57 3.57a1 1 0 0 1-.25 1z"/></svg>1234 567 890</li>
      <li><svg viewBox="0 0 24 24"><path d="M2 5h20v14H2z M2 6l10 7 10-7v2l-10 7L2 8z" fill-rule="evenodd"/></svg>mailid@webmail.com</li>
      <li><svg viewBox="0 0 24 24" style="fill:none;stroke:#ffffff;stroke-width:2"><circle cx="12" cy="12" r="9"/><path d="M3 12h18M12 3c3 3 3 15 0 18M12 3c-3 3-3 15 0 18"/></svg><span class="web">www.website.com</span></li>
      <li><svg viewBox="0 0 24 24"><path d="M12 2a7 7 0 0 0-7 7c0 5 7 13 7 13s7-8 7-13a7 7 0 0 0-7-7zm0 9.5A2.5 2.5 0 1 1 12 6.5a2.5 2.5 0 0 1 0 5z"/></svg><span>121/A, Address, Street<br>Pincode - 123456</span></li>
    </ul>

    <p class="front-wordmark">742BUILD</p>
  </section>

  <section class="card card--back">
    <div class="block ink rule-top"></div>
    <div class="block accent tab-top"></div>
    <div class="block accent tab-bottom"></div>
    <div class="block ink rule-bottom"></div>

    <p class="back-wordmark">742BUILD</p>
    <p class="tagline">Design and Renovation Firm</p>
  </section>
</body>
</html>
```